Construction Company

Design a clutter free business card, it can be double-sided utilizing the logo for BNX Ltd simple with all relevant contact information.

Please also a letterhead design to function for the purposes of invoicing, all mail requirements, with header to be distinctive while the footer ties page together and incorporates all necessary information.

For now, please use generic / dummy text and when a winner is selected, I will disclose the contact information.

Hi Designers! Please read the updated brief which includes the design of a business card and letterhead. Thank you!

```html
<!DOCTYPE html>
<html lang="en">
<head>
<meta charset="utf-8">
<title>BNX Ltd – Business Card</title>
<link rel="stylesheet" href="https://fonts.googleapis.com/css2?family=Inter:wght@400;500;700&display=swap">
<style>
  :root {
    --blue: #0b2fa3;
    --blue-deep: #08238a;
    --blue-light: #1a45c4;
    --gold: #b8901c;
    --gold-light: #d8b24a;
    --white: #ffffff;
    --stage: #1d1d1f;
  }
  * { box-sizing: border-box; margin: 0; padding: 0; }
  html, body { width: 1200px; height: 930px; overflow: hidden; }
  body {
    background: var(--stage);
    font-family: "Inter", Arial, sans-serif;
    position: relative;
  }
  .card {
    position: absolute;
    width: 560px;
    height: 320px;
    border-radius: 22px;
    overflow: hidden;
  }
  .card-front {
    left: 60px; top: 110px;
    background: linear-gradient(135deg, var(--blue-light) 0%, var(--blue) 45%, var(--blue-deep) 100%);
    display: flex; align-items: center; justify-content: center;
  }
  .card-back {
    left: 580px; top: 500px;
    background: linear-gradient(135deg, var(--blue-deep) 0%, var(--blue) 55%, var(--blue-light) 100%);
  }
  .card-back .backdrop { position: absolute; inset: 0; width: 100%; height: 100%; }

  .wordmark {
    display: flex; align-items: center; gap: 14px;
    font-weight: 700; letter-spacing: 1px;
  }
  .wordmark .mark-dot {
    width: 26px; height: 26px; border-radius: 50%;
    background: var(--gold);
  }
  .card-front .wordmark { font-size: 64px; color: var(--white); }
  .card-back .wordmark {
    position: absolute; left: 250px; top: 58px;
    font-size: 46px; color: var(--blue);
  }
  .card-back .wordmark .mark-dot { width: 20px; height: 20px; }

  .contact {
    position: absolute; left: 34px; bottom: 26px;
    color: var(--white);
  }
  .contact .name {
    color: var(--gold-light); font-weight: 700; font-size: 20px;
    letter-spacing: 0.5px; text-transform: uppercase;
  }
  .contact .role { font-size: 15px; margin-top: 2px; }
  .contact .address { font-size: 14px; line-height: 1.4; margin-top: 14px; }
  .contact .lines { list-style: none; margin-top: 10px; font-size: 14px; line-height: 1.5; }
  .contact .lines li { display: flex; align-items: center; gap: 8px; }
  .contact .lines svg { width: 13px; height: 13px; flex: none; }
</style>
</head>
<body>
  <section class="card card-front" aria-label="Business card front">
    <div class="wordmark"><span class="mark-dot"></span><span>BNX Ltd</span></div>
  </section>

  <section class="card card-back" aria-label="Business card back">
    <svg class="backdrop" viewBox="0 0 560 320" preserveAspectRatio="none" aria-hidden="true">
      <path d="M118,0 C175,150 350,225 560,212 L560,0 Z" fill="var(--white)"/>
      <path d="M110,0 C170,158 350,235 560,216" fill="none" stroke="var(--gold)" stroke-width="5"/>
    </svg>
    <div class="wordmark"><span class="mark-dot"></span><span>BNX Ltd</span></div>
    <div class="contact">
      <p class="name">Daniel Reed</p>
      <p class="role">Founder</p>
      <p class="address">820 Harbor Lane<br>Riverton, DE 19200</p>
      <ul class="lines">
        <li><svg viewBox="0 0 16 16"><path d="M4 1l3 3-2 2c1 2 3 4 5 5l2-2 3 3-2 3C7 15 1 9 1 3z" fill="var(--gold-light)"/></svg>(555) 014-2290</li>
        <li><svg viewBox="0 0 16 16"><rect x="1.5" y="3.5" width="13" height="9" fill="none" stroke="var(--gold-light)" stroke-width="1.5"/><path d="M1.5 3.5l6.5 5 6.5-5" fill="none" stroke="var(--gold-light)" stroke-width="1.5"/></svg>info@BNX Ltd.com</li>
        <li><svg viewBox="0 0 16 16"><circle cx="8" cy="8" r="6.5" fill="none" stroke="var(--gold-light)" stroke-width="1.5"/><path d="M1.5 8h13M8 1.5c-3 3.5-3 9.5 0 13M8 1.5c3 3.5 3 9.5 0 13" fill="none" stroke="var(--gold-light)" stroke-width="1.2"/></svg>www.BNX Ltd.com</li>
      </ul>
    </div>
  </section>
</body>
</html>
```